Design a menu for health restaurant

A health food restaurant in Los Angeles is seeking menu design. Our foods are made from scratch using whole ingredients.
Name: Grove Pantry
Address: 1000 E 60th StLos Angeles, CA 90347
Website: www.GrovePantry-example.com
We are looking for a clean and simple menu. Brand colors are white/tan, green and orange.

Please see attached excel with menu items and logo. We do not yet have prices.

Colors
f78f20
9bcb3c
ffffff
fff3d1

Requirements
Must have
• Easy to read.
Trifold menu design (front and back).
VEGAN, VEGETARIAN, GLUTEN FREE, CONTAINS NUTS symbols.
Logo.
Nice to have
• Incorporate brand colors, but still be easy to read.
We would like to use the Belco font (attached) if it works. If not we are open to a similar font that is easy to read.

Please see attached images.
We like the images and headers of OPTION 1. Would like something similar in trifold format.
We like the clean fonts of OPTION 2.

```html
<!DOCTYPE html>
<html lang="en">
<head>
<meta charset="utf-8">
<title>Grove Pantry – Menu</title>
<link href="https://fonts.googleapis.com/css2?family=Montserrat:wght@300;400;600;700&display=swap" rel="stylesheet">
<style>
:root{
  --paper:#f6f6f7;
  --green:#9bcb3c;
  --ink:#222;
  --ink-soft:#333;
  --rule:#9a9a9a;
  --veg:#2f6b2f;
  --vegan:#7fb241;
  --gf:#f3d21b;
  --nut:#f2a07f;
}
*{margin:0;padding:0;box-sizing:border-box}
html,body{width:1200px;height:848px;overflow:hidden;background:var(--paper)}
body{font-family:"Montserrat",sans-serif;color:var(--ink);position:relative}
.menu{position:relative;width:1200px;height:848px;border:1px solid var(--rule);overflow:hidden}
.fold{position:absolute;top:0;bottom:0;width:1px;background:var(--rule)}
.accent-bar{position:absolute;height:4px;width:132px;background:var(--green)}
.section-title{position:absolute;font-weight:300;font-size:31px;line-height:30px;color:var(--green);letter-spacing:-.5px;z-index:2}
.photo{position:absolute;width:216px;height:108px;border-radius:0 0 108px 108px;z-index:1}
.items{position:absolute;list-style:none}
.item{margin-bottom:8px}
.item-name{font-weight:600;font-size:12px;line-height:14px;color:var(--ink);display:flex;align-items:center;flex-wrap:wrap}
.item-name .price{font-weight:400;margin-left:10px}
.item-desc{font-size:9.1px;line-height:12px;color:var(--ink-soft)}
.badge{display:inline-flex;align-items:center;justify-content:center;width:10px;height:10px;border-radius:50%;font-size:5px;font-weight:700;margin-left:3px;line-height:1}
.badge.v{background:var(--veg);color:#fff}
.badge.vg{background:var(--vegan);color:#1d3d12}
.badge.gf{background:var(--gf);color:#5a4a00}
.badge.n{background:var(--nut);color:#8a2b12}
.produce{position:absolute;left:0;top:742px;width:400px;height:106px;background:linear-gradient(90deg,#3f7d2c,#c9b23c 30%,#e4e4e4 50%,#d6322a 70%,#5b9a3a)}
.legend{position:absolute;top:818px;left:444px;display:flex;font-size:8px;align-items:center}
.legend li{list-style:none;display:flex;align-items:center;margin-right:26px}
.legend .badge{margin:0 6px 0 0}
</style>
</head>
<body>
<main class="menu">
  <div class="fold" style="left:400px"></div>
  <div class="fold" style="left:800px"></div>

  <!-- Panel 1 -->
  <div class="accent-bar" style="left:29px;top:25px"></div>
  <div class="photo" role="img" aria-label="Grain bowl with vegetables and falafel" style="left:161px;top:25px;background:radial-gradient(circle at 60% 30%,#d78b3a,#6b7a3a 45%,#2c3440 85%)"></div>
  <h2 class="section-title" style="left:30px;top:63px">BOWLS</h2>
  <ul class="items" style="left:29px;top:117px;width:335px">
    <li class="item"><div class="item-name">Southwest Bowl<span class="badge gf">GF</span><span class="badge n">N</span><span class="price">0.00</span></div><p class="item-desc">Your choice of protein with corn, black beans, red onions, almonds and avocado over quinoa with lime hot sauce.</p></li>
    <li class="item"><div class="item-name">Chimi Bowl<span class="badge gf">GF</span><span class="price">0.00</span></div><p class="item-desc">Your choice of protein with red bell pepper, mushrooms, zucchini, squash, onion, cherry tomatoes and fresh herb chimichurri on wild and brown rice.</p></li>
    <li class="item"><div class="item-name">Soba Noodle Bowl<span class="price">0.00</span></div><p class="item-desc">Your choice of protein with spinach, snow peas, roasted carrots, red bell pepper, cilantro, sesame seeds and ginger lime sauce over soba noodles.</p></li>
    <li class="item"><div class="item-name">Hollywood Bowl<span class="badge gf">GF</span><span class="price">0.00</span></div><p class="item-desc">Your choice of protein with broccoli, roasted corn, cherry tomatoes, basil, pepitas, flax seeds and lemon juice on wild and brown rice.</p></li>
    <li class="item"><div class="item-name">Grove Bowl<span class="badge gf">GF</span><span class="price">0.00</span></div><p class="item-desc">Your choice of protein with roasted chickpeas and cauliflower, zesty fennel salad and citrus yogurt.</p></li>
    <li class="item"><div class="item-name">Buddha Bowl<span class="price">0.00</span></div><p class="item-desc">Your choice of protein with corn, red kale, sweet potatoes, red cabbage, parsley, oregano, hummus, and farro.</p></li>
    <li class="item"><div class="item-name">Chili Rice Bowl<span class="badge gf">GF</span><span class="price">0.00</span></div><p class="item-desc">Chicken, onions, bell peppers, jalapeños, black &amp; kidney beans, and tomato over brown rice.</p></li>
  </ul>

  <div class="accent-bar" style="left:29px;top:474px"></div>
  <div class="photo" role="img" aria-label="Grilled wrap with lime and peppers" style="left:161px;top:474px;background:radial-gradient(circle at 60% 35%,#e3c79a,#b0733a 45%,#3a3430 85%)"></div>
  <h2 class="section-title" style="left:28px;top:514px">WRAPS</h2>
  <ul class="items" style="left:29px;top:566px;width:335px">
    <li class="item"><div class="item-name">Rancher's Wrap<span class="price" style="margin-left:30px">0.00</span></div><p class="item-desc">Tomato, red onion, hard boiled egg, avocado,<br>feta cheese, microgreens, romaine, grilled chicken and Ranch dressing in a grilled wrap.</p></li>
    <li class="item"><div class="item-name">Vegan Tuna Wrap<span class="badge vg">VG</span><span class="price">0.00</span></div><p class="item-desc">Vegan tuna, romaine, avocado, celery, shallot, and oregano with Herbali-cious Sauce in a whole grain wrap.</p></li>
    <li class="item"><div class="item-name">Vegetarian Wrap<span class="badge v">V</span><span class="price">0.00</span></div><p class="item-desc">Roasted chickpeas, romaine, avocado, red bell pepper, shaved carrots, cucumber, spinach, basil, black beans and feta with lemon-hummus in a sprouted 7-grain wrap.</p></li>
  </ul>
  <div class="produce" role="img" aria-label="Fresh vegetables: eggplant, peppers, corn, asparagus"></div>

  <!-- Panel 2 -->
  <div class="accent-bar" style="left:431px;top:25px"></div>
  <div class="photo" role="img" aria-label="Fresh salad with strawberries and feta" style="left:565px;top:25px;background:radial-gradient(circle at 50% 30%,#e9e9e9,#7fae4a 40%,#c8cdd2 85%)"></div>
  <h2 class="section-title" style="left:431px;top:63px">SALAD</h2>
  <ul class="items" style="left:431px;top:116px;width:340px">
    <li class="item"><div class="item-name">Avocado, Golden Beet,<br>and Cranberry Salad<span class="badge v">V</span><span class="badge gf">GF</span><span class="price">0.00</span></div><p class="item-desc">Gold beets, avocado, dried cranberries, watermelon radish, red kale, romaine, mixed greens, and pepitas served with Golden Buddha dressing.</p></li>
    <li class="item"><div class="item-name">Burrata Salad<span class="badge v">V</span><span class="badge gf">GF</span><span class="price">0.00</span></div><p class="item-desc">Tomato, melon, shredded basil, balsamic glaze, fresh cracked pepper, and olive oil with burrata.</p></li>
    <li class="item"><div class="item-name">Mediterranean Salad<span class="badge v">V</span><span class="badge gf">GF</span><span class="price">0.00</span></div><p class="item-desc">Cucumbers, Kalamata olives, cherry tomatoes, parsley, tricolor quinoa, hard-boiled egg, and hummus on mixed greens, romaine, and red cabbage with lemon-olive oil dressing.</p></li>
    <li class="item"><div class="item-name">Vegan Chef Salad<span class="badge vg">VG</span><span class="badge gf">GF</span><span class="badge n">N</span><span class="price">0.00</span></div><p class="item-desc">Roasted potatoes and carrots, chickpeas, avocado, microgreens and walnuts on mixed greens, romaine, and red kale with vegan ranch.</p></li>
    <li class="item"><div class="item-name">Rancher's Salad<span class="badge v">V</span><span class="badge gf">GF</span><span class="price">0.00</span></div><p class="item-desc">Tomato, red onion, hard boiled egg, avocado, feta cheese, microgreens, and grilled chicken on romaine with Ranch dressing.</p></li>
  </ul>

  <div class="accent-bar" style="left:431px;top:410px"></div>
  <div class="photo" role="img" aria-label="Burgers on a wooden board" style="left:562px;top:410px;background:radial-gradient(circle at 50% 30%,#d9a25a,#8a5a2a 45%,#232323 85%)"></div>
  <h2 class="section-title" style="left:432px;top:433px">BURGERS<br>N' SAMMIES</h2>
  <ul class="items" style="left:431px;top:516px;width:340px">
    <li class="item"><div class="item-name">Air Fried Chicken Sammy<span class="price" style="margin-left:28px">0.00</span></div><p class="item-desc">Air fried chicken breast topped with<br>red leaf lettuce, tomato, house made pickles and Grove Sauce on a bun served with choice of salad of fries.</p></li>
    <li class="item"><div class="item-name">Grilled Chicken Sammy<span class="price" style="margin-left:36px">0.00</span></div><p class="item-desc">Grilled chicken topped with guacamole, red leaf lettuce, tomato, house made pickles and Grove Sauce. Served with regular fries or side salad.</p></li>
    <li class="item"><div class="item-name">Classic Beef Burger<span class="price" style="margin-left:36px">0.00</span></div><p class="item-desc">House seasoned beef burger topped with red leaf lettuce, tomato, cheddar cheese, house made pickles and Grove Sauce on a bun served with choice of salad of fries.</p></li>
    <li class="item"><div class="item-name">Black Bean Pine Nut Burger<span class="badge vg">VG</span><span class="badge n">N</span><span class="price">0.00</span></div><p class="item-desc">House made black bean pine nut burger topped with red leaf lettuce, tomato, house made pickles and mustard aioli on a bun served with choice of salad of fries.</p></li>
    <li class="item"><div class="item-name">Salmon Burger<span class="price" style="margin-left:36px">0.00</span></div><p class="item-desc">House made salmon burger topped with red leaf lettuce, tomato, house made pickles and Grove yogurt on a bun served with choice of salad of fries.</p></li>
  </ul>

  <ul class="legend">
    <li><span class="badge v">V</span>Vegetarian</li>
    <li><span class="badge vg">VG</span>Vegan</li>
    <li><span class="badge gf">GF</span>Gluten Free</li>
    <li><span class="badge n">N</span>Contains Nuts</li>
  </ul>

  <!-- Panel 3 -->
  <div class="accent-bar" style="left:829px;top:25px"></div>
  <div class="photo" role="img" aria-label="Fries with dipping sauces" style="left:961px;top:25px;background:radial-gradient(circle at 65% 30%,#e6a43a,#8a5a32 50%,#5a3a26 85%)"></div>
  <h2 class="section-title" style="left:829px;top:46px">SNACKS<br>N' SIDES</h2>
  <ul class="items" style="left:829px;top:132px;width:325px">
    <li class="item"><div class="item-name">Fries<span class="badge v">V</span><span class="badge gf">GF</span><span class="price">0.00</span></div><p class="item-desc">Hand cut air-fries with house seasonings. Choose regular or sweet potato fries.</p></li>
    <li class="item"><div class="item-name">Side Salad<span class="badge v">V</span><span class="price" style="margin-left:28px">0.00</span></div><p class="item-desc">Your choice of House, Golden Beet, Mediterranean, or Vegan Chef side salad. (24oz)</p></li>
    <li class="item"><div class="item-name">Guac + Chips<span class="badge v">V</span><span class="badge gf">GF</span><span class="price">0.00</span></div><p class="item-desc">Guacamole with blue corn tortilla chips.</p></li>
    <li class="item"><div class="item-name">Hummus + Chips<span class="badge v">V</span><span class="badge gf">GF</span><span class="price">0.00</span></div><p class="item-desc">Hummus with blue corn tortilla chips.</p></li>
  </ul>

  <div class="accent-bar" style="left:829px;top:313px"></div>
  <div class="photo" role="img" aria-label="Tomato soup with bread basket" style="left:963px;top:311px;background:radial-gradient(circle at 55% 45%,#e07a3a,#a0754a 45%,#4a3a2c 85%)"></div>
  <h2 class="section-title" style="left:831px;top:341px">COMBOS</h2>
  <ul class="items" style="left:831px;top:394px;width:210px">
    <li class="item"><div class="item-name">Soup + Salad<span class="price" style="margin-left:36px">0.00</span></div><p class="item-desc">"Your choice of soup and side salad.<br>16oz soup + 38oz salad"</p></li>
    <li class="item"><div class="item-name">Avo Toast Combo<span class="price" style="margin-left:36px">0.00</span></div><p class="item-desc" style="width:200px">Half avocado toast and your choice of soup. 16oz</p></li>
    <li class="item"><div class="item-name">Soup + Sammy<span class="price" style="margin-left:36px">0.00</span></div><p class="item-desc">"Your choice of soup and sandwich.<br>16oz soup + Sandwich"</p></li>
  </ul>

  <div class="accent-bar" style="left:829px;top:551px"></div>
  <div class="photo" role="img" aria-label="Slice of layered carrot cake" style="left:963px;top:551px;background:radial-gradient(circle at 55% 35%,#c07a3e,#8a4a26 45%,#d8c2b2 85%)"></div>
  <h2 class="section-title" style="left:829px;top:580px">DESSERTS</h2>
  <ul class="items" style="left:829px;top:636px;width:325px">
    <li class="item"><div class="item-name">Date Coffee Cake<span class="badge v">V</span><span class="badge gf">GF</span><span class="price">0.00</span></div><p class="item-desc">Signature date coffee cake with walnuts.</p></li>
    <li class="item"><div class="item-name">Fruit + Spices<span class="badge vg">VG</span><span class="badge gf">GF</span><span class="price">0.00</span></div><p class="item-desc">Strawberry, pineapple, green apple, orange, and blueberries with lime and chili seasoning.</p></li>
    <li class="item"><div class="item-name">Cookies<span class="badge v">V</span><span class="price" style="margin-left:26px">0.00</span></div><p class="item-desc">Your choice of Chocolate Chip or Double Chocolate Chip fresh baked cookie.</p></li>
    <li class="item"><div class="item-name">Grove Chocolate Mousse<span class="badge vg">VG</span><span class="badge gf">GF</span><span class="price">0.00</span></div><p class="item-desc">Served with grated dark chocolate.</p></li>
  </ul>
</main>
</body>
</html>
```